Wordpress Design Project

Utilising the WORDPRESS Open source software, make changes to the current site to reflect current business and marketing plan.

This includes the actual structure and layout- less words and more images (not sure what). Also to provide link to most appropriate blog which would incorporate all my posts on Linked
In, which is the main focus of my "commentary" on various topics given that I am a B to B operation. Review my current blog- "thoughts"- maybe get rid of it.

I have a Facebook fan page and a plain circle site and the site already has links to those, but I really don't utilise them much. You will not that I have top SEO ranking on google, both the business name and my name.

Go to http://www.tbartworksadvisory.example

Thanks

Gordon Huxtable
Updates

Hi there

Having reviewed all submissions there is one key issue- stock business images. While I recognise I am a business, I have tried to differentiate myself from other businesses by showing myself as a bit more "arty". 

Lots of images of happy business people is not my style.

In most submissions the structure and function looks good through.

Thanks

Gordon

                                

From a colleague of mine:                                    

my overall impression is that it is all very corporate...perfect white teeth, squeaky clean and

far too many ties. Having worked in the arts for over 20 years none of the concepts is really reflective of the reality of working in the arts. Quirky, cutting edge, sophisticated in unique ways rather

than clichéd ways, beautiful, inspiring challenging...etc

Thanks

Gordon

I imagine gorgeous uplifting images from across

arts disciplines images, kids doing creative things, street art, gorgeous

dancers in mid flight, great public art, community, collaboration and maybe one

or two ties! Does this help?

 

F

                                       

All current designs are too corporate.

I sell business solutions to organisations that are engaged with the development and production of creative goods and services. Art, Theatre, Dance, Architecture, Community Festivals, Events, Creative Innovation Hubs.

I also help build bridges between the creative sector and business- for businesses who want create affiliations with arts to enhance their business and for the creative sector to receive in return goods and services or for joint venture purposes.

The site needs to show artistic flair, design sensibility and business acumen and strength. Some of these designs are on the right track

http://www.pixelgrove.example/article/50-best-creative-websites-of-2011/4144/

Many thanks

Gordon

                                       

I have made some updates to my current site which better reflect what I am on about. now. There are some important key words there now

http://www.tbartworksadvisory.example

ow.                                   

                                       

ow.                                   

Target Market(s)

Business to Business but most customers will be educated and into cultural pursuits, theatre, opera, good food, wine, education

Industry/Entity Type

Marketing

Requirements
Must have
• Needs to show me as who I am- a bit different- think of Van Rusk,
Nice to have
• Originality and appropriate links to social media
Blog
Should not have
• Sock standard business images

```html
<!DOCTYPE html>
<html lang="en">
<head>
<meta charset="utf-8">
<title>TB Artworks Advisory</title>
<link rel="stylesheet" href="https://fonts.googleapis.com/css2?family=Roboto+Condensed:wght@300;400;700&family=Crimson+Text:ital@0;1&display=swap">
<style>
:root{
  --red:#b5182b;
  --ink:#222;
  --body:#333;
  --orange:#ef8a17;
  --cyan:#22c3d3;
  --green:#1f8a3b;
  --green-dark:#0e3d1c;
  --footer:#3f4650;
  --footer-text:#6c737c;
  --social:#8a9098;
  --white:#fff;
}
*{margin:0;padding:0;box-sizing:border-box}
html,body{width:696px;height:1200px;overflow:hidden;background:var(--white)}
body{position:relative;font-family:"Roboto Condensed",Arial,sans-serif;color:var(--body)}
.abs{position:absolute}

.brand{left:83px;top:16px;display:flex;align-items:center;gap:8px}
.brand-mark{width:18px;height:18px;background:var(--ink)}
.brand-name{font-size:16px;font-weight:700;color:var(--ink);line-height:17px}
.contact{left:397px;top:18px;font-size:8px;color:var(--ink);white-space:nowrap}
.utility-nav{left:473px;top:48px;display:flex;gap:11px;font-size:8px;color:var(--ink)}

.main-nav{left:0;top:89px;width:696px;height:23px;background:var(--red)}
.main-nav span{position:absolute;top:0;line-height:23px;font-size:10px;font-weight:700;color:var(--white);white-space:nowrap}

.hero{left:0;top:112px;width:696px;height:181px;
  background:
    linear-gradient(rgba(40,34,30,.25),rgba(40,34,30,.35)),
    linear-gradient(90deg,#3c3531 0,#9b8577 8%,#5a4f49 15%,#b09886 24%,#4a423e 32%,#8e7a6c 41%,#6a5e56 50%,#a58f80 59%,#4f4743 68%,#987f71 77%,#5c524c 86%,#a28c7e 93%,#2e2926 100%)}
.hero-title{left:0;top:127px;width:696px;text-align:center;font-size:48px;font-weight:700;line-height:55px;color:var(--white);letter-spacing:-.2px;text-shadow:0 1px 3px rgba(0,0,0,.3)}

.card{top:263px;width:147px;height:214px;background:var(--white);box-shadow:0 0 3px rgba(0,0,0,.22)}
.card-tab{height:30px;color:var(--white);font-size:12.5px;font-weight:400;text-align:center;line-height:30px;white-space:nowrap}
.card p{font-size:8.2px;line-height:12.6px;text-align:center;padding:5px 11px 0;color:var(--ink)}
.card-link{position:absolute;left:12px;right:12px;bottom:7px;height:11px;font-size:7.2px;line-height:11px;text-align:center;color:var(--white);white-space:nowrap;clip-path:polygon(4% 0,96% 0,100% 50%,96% 100%,4% 100%,0 50%)}
.orange{background:var(--orange)}.cyan{background:var(--cyan)}.green{background:var(--green)}

.headline{left:104px;top:502px;font-size:35px;font-weight:700;line-height:40px;white-space:nowrap}
.headline .l1{display:block;background:linear-gradient(90deg,#55297f 0,#8a2f86 38%,#c8345a 62%,#b0203a 85%,#8e1a34 100%);-webkit-background-clip:text;background-clip:text;color:transparent}
.headline .l2{display:block;margin-left:105px;width:245px;background:linear-gradient(90deg,#b04aa0,#e0457a 50%,#d8283f);-webkit-background-clip:text;background-clip:text;color:transparent}

.intro{left:83px;top:614px;width:532px;font-size:10.6px;line-height:17.3px;color:var(--ink);font-weight:400}
.intro p+p{margin-top:16px}
.read-more{left:312px;top:760px;width:72px;height:15px;border-radius:8px;background:linear-gradient(#f4f4f4,#c9c9c9);box-shadow:0 1px 2px rgba(0,0,0,.2);font-size:7.5px;font-weight:700;text-align:center;line-height:15px;color:#444}
.divider{left:70px;top:796px;width:556px;height:20px;background:radial-gradient(ellipse at 50% 0,rgba(0,0,0,.16),rgba(0,0,0,0) 70%)}

.tweet{left:216px;top:858px;display:flex;align-items:center;gap:9px;font-family:"Crimson Text",Georgia,serif;font-size:12.5px;color:var(--ink)}
.tweet-dot{width:19px;height:19px;border-radius:50%;background:#3aa0d8}
.tweet em{color:#2aa6c8}

.signup{left:195px;top:924px}
.signup-field{left:220px;top:993px;width:172px;height:31px;background:var(--white);border-radius:2px;font-family:"Crimson Text",Georgia,serif;font-style:italic;font-size:11.5px;color:#888;padding:7px 10px}
.signup-btn{left:400px;top:993px;width:77px;height:31px;background:var(--green-dark);color:var(--white);font-size:11.5px;text-align:center;line-height:31px}

.footer{left:0;top:1053px;width:696px;height:147px;background:var(--footer)}
.top-tab{left:331px;top:1053px;width:34px;height:28px;background:#9ba1a8;clip-path:polygon(0 0,100% 0,100% 72%,50% 100%,0 72%);color:var(--white);font-size:6.5px;font-weight:700;text-align:center;line-height:18px}
.footer-nav{left:0;top:1101px;width:696px;text-align:center;font-size:8.5px;font-weight:700;color:var(--footer-text)}
.copyright{left:0;top:1131px;width:696px;text-align:center;font-size:8px;font-weight:700;color:var(--footer-text)}
.social{left:298px;top:1161px;display:flex;gap:9px}
.social span{width:18px;height:18px;border-radius:50%;background:var(--social)}
</style>
</head>
<body>
<header>
  <div class="abs brand"><span class="brand-mark"></span><span class="brand-name">TB Artworks<br>Advisory</span></div>
  <div class="abs contact">T +610 5550 1842 &nbsp;|&nbsp; F +610 5550 1842 &nbsp;|&nbsp; M +610 5550 2967</div>
  <nav class="abs utility-nav"><span>Home</span><span>Our Team</span><span>Clients</span><span>Contact</span></nav>
</header>

<nav class="abs main-nav">
  <span style="left:96px">Helping you Plan</span>
  <span style="left:190px">Creative Strategy</span>
  <span style="left:287px">Implementing your plans</span>
  <span style="left:413px">Workshops</span>
  <span style="left:484px">Projects</span>
  <span style="left:543px">Our Thoughts</span>
</nav>

<div class="abs hero" role="img" aria-label="Banner photograph: a grid of portraits of creative people"></div>
<h1 class="abs hero-title">Innovation, Enterprise and<br>Creative Strategy</h1>

<section class="abs card" style="left:83px">
  <div class="card-tab orange">Creative Organisations</div>
  <p>Are you a not for profit arts organisation looking for long-term stability and success, creatively and financially? We can assist by keeping your objectives and financial viability in balance. We'll help you adopt strong business principles and procedures to ensure your future growth. We can also help you develop mutually beneficial partnerships with business.</p>
  <div class="card-link orange">How we help Creative Organisations</div>
</section>
<section class="abs card" style="left:275px">
  <div class="card-tab cyan">Creative Business</div>
  <p>Are you a new or growing creative business that needs help with your direction? We can show you how to adopt world's best practice principles and support the development of your creative practice to help you achieve greater exposure and long term returns- including better sales results.</p>
  <div class="card-link cyan">How we help Creative Business</div>
</section>
<section class="abs card" style="left:467px">
  <div class="card-tab green">Creative Communities</div>
  <p>Are you a creative community that needs direction to help you get creative projects off the ground? We work with community groups and local Councils to assist in the development and implementation of policy related to creative community programs. This includes Festivals, Events and Public Art Programs. We also try to ensure that projects we support will have long term impacts and lasting economic benefits.</p>
  <div class="card-link green">How we help Creative Communities</div>
</section>

<h2 class="abs headline"><span class="l1">How to maximise the potential of</span><span class="l2">your organisation</span></h2>

<div class="abs intro">
  <p>TB Artworks Advisory is a business consultancy dedicated to helping businesses within the arts, cultural and creative industries develop the business tools they need to achieve their creative vision. We also work with communities at at local government level, supporting the development of policy in relation to events, festivals and public art programs.</p>
  <p>Another component of our business is to support other businesses seeking an alignment with arts projects as part of their company's marketing objectives. To this end TB Artworks Advisory has worked with NCEF (National Culture Enterprise Fund) now Arts Alliance Partners on developing partnership proposals with companies wanting brand alignment with arts companies.</p>
</div>
<div class="abs read-more">Read More &#9656;</div>
<div class="abs divider"></div>

<div class="abs tweet"><span class="tweet-dot"></span><span>"No public messages." <em>- tbartworksadv</em></span></div>

<svg class="abs signup" width="312" height="130" viewBox="0 0 312 130"><path d="M0 130 V60 Q0 54 6 52 L288 0 Q298 -2 299 8 L312 130 Z" fill="#1f8a3b"/></svg>
<div class="abs signup-field">Type your email here...</div>
<div class="abs signup-btn">SUBSCRIBE</div>

<footer class="abs footer"></footer>
<div class="abs top-tab">TOP</div>
<div class="abs footer-nav">Home &nbsp;-&nbsp; Helping you Plan &nbsp;-&nbsp; Creative Strategy &nbsp;-&nbsp; Implementing your plans &nbsp;-&nbsp; Workshops &nbsp;-&nbsp; Projects &nbsp;-&nbsp; Our Team &nbsp;-&nbsp; Clients &nbsp;-&nbsp; Our Thoughts</div>
<div class="abs copyright">Copyright © 2013 TB Artworks Advisory. All Rights Reserved.</div>
<div class="abs social"><span></span><span></span><span></span><span></span></div>
</body>
</html>
```